Analytics software company needs a business card design

We need a business card design for a global analytics software provider called 'Varnel Software'. Our main focus is developing real estate analysis software. We are open to any color scheme. The final design should be simple, modern, and precise.
Updates

There is one day left in our project and we are still looking forward to receiving additional submissions. We look forward to selecting one of your designs. Thanks.

Industry/Entity Type

Real Estate

```html
<!DOCTYPE html>
<html lang="en">
<head>
<meta charset="utf-8">
<title>Varnel Software – Business Card</title>
<link rel="stylesheet" href="https://fonts.googleapis.com/css2?family=Roboto:wght@400;500;700&display=swap">
<style>
  :root {
    --page-bg: #e9ebee;
    --card-bg: #ffffff;
    --blue-deep: #1f4fb0;
    --blue-mid: #2f78d2;
    --blue-light: #5aa7ea;
    --green: #3f9a2a;
    --green-light: #8cc63f;
    --ink: #3a3f47;
    --ink-soft: #5b6270;
    --brand: #1f5fb8;
  }
  * { margin: 0; padding: 0; box-sizing: border-box; }
  html, body { width: 1200px; height: 899px; overflow: hidden; }
  body {
    background: var(--page-bg);
    font-family: "Roboto", Arial, sans-serif;
    display: flex; align-items: center; justify-content: center;
  }
  .card {
    position: relative;
    width: 900px; height: 514px;
    background: var(--card-bg);
    border-radius: 40px;
    overflow: hidden;
    box-shadow: 0 10px 30px rgba(0,0,0,.15);
  }
  .card__band { position: absolute; inset: 0; width: 100%; height: 100%; }
  .holder {
    position: absolute; right: 60px; top: 70px;
    text-align: right; color: #fff;
  }
  .holder__name { font-size: 34px; font-weight: 500; letter-spacing: 2px; }
  .holder__role { font-size: 21px; font-weight: 400; margin-top: 6px; }
  .brand {
    position: absolute; left: 60px; top: 170px;
    display: flex; align-items: center; gap: 16px;
  }
  .brand__dot {
    width: 66px; height: 66px; border-radius: 50%;
    background: var(--green);
  }
  .brand__name {
    font-size: 40px; font-weight: 700; color: var(--brand);
    line-height: 1;
  }
  .contacts {
    position: absolute; left: 60px; top: 295px;
    list-style: none;
    font-size: 15px; color: var(--ink);
  }
  .contacts li { display: flex; align-items: center; gap: 12px; height: 30px; }
  .contacts svg { width: 16px; height: 16px; fill: var(--ink-soft); }
  .address {
    position: absolute; right: 60px; bottom: 50px;
    text-align: right; font-size: 18px; color: var(--ink); line-height: 1.45;
  }
</style>
</head>
<body>
  <article class="card">
    <svg class="card__band" viewBox="0 0 900 514" preserveAspectRatio="none" aria-hidden="true">
      <defs>
        <linearGradient id="bandBlue" x1="0" y1="0" x2="1" y2="0.3">
          <stop offset="0" stop-color="var(--blue-light)"/>
          <stop offset="0.5" stop-color="var(--blue-mid)"/>
          <stop offset="1" stop-color="var(--blue-deep)"/>
        </linearGradient>
        <linearGradient id="bandGreen" x1="0" y1="0" x2="1" y2="0">
          <stop offset="0" stop-color="var(--green-light)"/>
          <stop offset="1" stop-color="var(--green)"/>
        </linearGradient>
      </defs>
      <path d="M0 0 H900 V300 C760 200 520 120 260 118 C150 117 60 130 0 150 Z" fill="url(#bandBlue)"/>
      <path d="M0 150 C60 130 150 117 260 118 C520 120 760 200 900 300 V322 C760 222 520 140 260 138 C150 137 60 150 0 170 Z" fill="url(#bandGreen)"/>
    </svg>

    <header class="holder">
      <h1 class="holder__name">DANIEL HARTWELL</h1>
      <p class="holder__role">Managing Director</p>
    </header>

    <div class="brand">
      <span class="brand__dot"></span>
      <span class="brand__name">Varnel Software</span>
    </div>

    <ul class="contacts">
      <li><svg viewBox="0 0 16 16"><path d="M3 1h3l1 4-2 1c1 2 3 4 5 5l1-2 4 1v3c0 1-1 2-2 2C7 15 1 9 1 3c0-1 1-2 2-2z"/></svg>020 481 3370</li>
      <li><svg viewBox="0 0 16 16"><path d="M4 0h8a1 1 0 0 1 1 1v14a1 1 0 0 1-1 1H4a1 1 0 0 1-1-1V1a1 1 0 0 1 1-1zm1 2v10h6V2z"/></svg>020 481 3370</li>
      <li><svg viewBox="0 0 16 16"><path d="M4 1h8v4H4zM1 6h14v7h-3v2H4v-2H1zm4 4v4h6v-4z"/></svg>020 481 3370</li>
      <li><svg viewBox="0 0 16 16"><path d="M1 3h14v10H1zm1 1v1l6 4 6-4V4z"/></svg>mail@varnelsoft.com</li>
      <li><svg viewBox="0 0 16 16"><path d="M8 0a8 8 0 1 0 0 16A8 8 0 0 0 8 0zm0 1.5c1 1.3 1.7 3.2 1.8 5.5H6.2C6.3 4.7 7 2.8 8 1.5zM1.6 7a6.5 6.5 0 0 1 3.6-5A12 12 0 0 0 4.7 7zm0 2h3.1c.1 1.9.6 3.6 1.5 5a6.5 6.5 0 0 1-4.6-5zm4.6 0h3.6c-.1 2.3-.8 4.2-1.8 5.5C7 13.2 6.3 11.3 6.2 9zm5.1 0h3.1a6.5 6.5 0 0 1-4.6 5c.9-1.4 1.4-3.1 1.5-5zm0-2a12 12 0 0 0-.5-5 6.5 6.5 0 0 1 3.6 5z"/></svg>www.varnelsoft.com</li>
    </ul>

    <address class="address" style="font-style:normal">
      B12,9th floor,Arcade<br>Harbour Lane NTH
    </address>
  </article>
</body>
</html>
```